BrivoMatex. Lantern for the Steady Growth. Business card

Professional business card for BrivoMatex (Lantern for the Steady Growth)
My rationale: Strategy-> Execution-> Results-> Value that lead to the BrivoMatex name: We put the Lantern for the Steady Growth.
We deliver value to our customers helping them at defining a good strategy (cyan arrow). 90% of well formulated strategies fail due to poor execution so we also consider strategical execution very important (green arrow). Due to the execution we obtain the results (blue arrow). Finally, the results provide feedback to redefine strategy, and the new strategy has to be executed and new results obtained providing new feedback and on and on. It's like a wheel that finally, must create corporate value: value for shareholders, staholders, employees, providers...-

Target Market(s)

CEOs and steering comitees , invewrnent funds

Industry/Entity Type

Business Consultant

Contact Information for Business Card

Tommaso Ferlini
CEO & Founder
tommaso.ferlini@brivomatex.example
Mobile: +34 611.205.938
www.brivomatex.example

Colors

Designer to choose colors to be used in the design.

Requirements
Nice to have
• Nice to hace the words: Strategy, execution, results
• Nice to vave the claim: Lantern for the Steady Growth
• The three colors should be shown:
• cyan for STRATEGY
• green for EXECUTION
• blue for RESULTS
Should not have
• Complete black background

```html
<!DOCTYPE html>
<html lang="en">
<head>
<meta charset="UTF-8">
<title>BrivoMatex — Business Card</title>
<link href="https://fonts.googleapis.com/css2?family=Ubuntu:wght@400;500;700&display=swap" rel="stylesheet">
<style>
  :root {
    --stage: #2b2b2e;
    --brand-blue: #25409a;
    --brand-blue-light: #3a5cb8;
    --brand-green: #8dc63f;
    --brand-cyan: #29abe2;
    --paper: #ffffff;
    --text-blue: #25409a;
  }
  * { box-sizing: border-box; margin: 0; padding: 0; }
  html, body {
    width: 1200px;
    height: 880px;
    overflow: hidden;
    background: var(--stage);
    font-family: "Ubuntu", sans-serif;
  }
  .stage { position: relative; width: 1200px; height: 880px; }
  .card {
    position: absolute;
    width: 620px;
    height: 354px;
    border-radius: 16px;
    overflow: hidden;
  }
  .card--front {
    left: 70px;
    top: 60px;
    background: linear-gradient(135deg, var(--brand-blue-light) 0%, var(--brand-blue) 45%, var(--brand-blue) 100%);
    color: var(--paper);
  }
  .front__glow {
    position: absolute;
    left: -80px;
    top: -60px;
    width: 360px;
    height: 420px;
    background: radial-gradient(closest-side, rgba(255,255,255,0.14), rgba(255,255,255,0));
  }
  .front__brand {
    position: absolute;
    left: 0; right: 0;
    top: 118px;
    display: flex;
    justify-content: center;
    align-items: center;
    gap: 16px;
  }
  .front__dot {
    width: 26px;
    height: 26px;
    border-radius: 50%;
    background: var(--brand-green);
    flex: none;
  }
  .front__name {
    font-weight: 700;
    font-size: 64px;
    letter-spacing: -1px;
    color: var(--paper);
  }
  .front__web {
    position: absolute;
    left: 0; right: 0;
    top: 250px;
    text-align: center;
    font-size: 17px;
    letter-spacing: 0.5px;
    color: var(--paper);
  }
  .card--back {
    left: 510px;
    top: 466px;
    background: var(--paper);
  }
  .back__bands {
    position: absolute;
    right: 0;
    top: 0;
    width: 320px;
    height: 354px;
  }
  .back__name {
    position: absolute;
    left: 44px;
    top: 88px;
    font-weight: 700;
    font-size: 56px;
    letter-spacing: -1px;
    color: var(--text-blue);
  }
  .contact { position: absolute; left: 44px; top: 200px; }
  .contact__person { font-weight: 500; font-size: 22px; color: var(--text-blue); }
  .contact__role { font-size: 15px; color: var(--brand-green); margin-top: 2px; margin-bottom: 8px; }
  .contact__line {
    display: flex;
    align-items: center;
    gap: 8px;
    font-size: 15px;
    line-height: 24px;
    color: var(--text-blue);
  }
  .contact__icon { width: 14px; height: 14px; flex: none; }
</style>
</head>
<body>
<main class="stage">
  <section class="card card--front" aria-label="Business card front">
    <div class="front__glow"></div>
    <div class="front__brand">
      <span class="front__dot"></span>
      <span class="front__name">BrivoMatex</span>
    </div>
    <div class="front__web">www.brivomatex.example</div>
  </section>

  <section class="card card--back" aria-label="Business card back">
    <svg class="back__bands" viewBox="0 0 320 354" aria-hidden="true">
      <rect class="band band--results" x="20" y="40" width="300" height="52" fill="var(--brand-blue)"/>
      <rect class="band band--execution" x="90" y="124" width="230" height="46" fill="var(--brand-green)"/>
      <rect class="band band--strategy" x="160" y="200" width="160" height="40" fill="var(--brand-cyan)"/>
    </svg>
    <div class="back__name">BrivoMatex</div>
    <div class="contact">
      <div class="contact__person">Tommaso Ferlini</div>
      <div class="contact__role">CEO &amp; Founder</div>
      <div class="contact__line">
        <svg class="contact__icon" viewBox="0 0 24 24" aria-hidden="true"><path fill="#8dc63f" d="M6.6 10.8a15.1 15.1 0 0 0 6.6 6.6l2.2-2.2c.3-.3.7-.4 1-.2 1.1.4 2.3.6 3.6.6.6 0 1 .4 1 1V20c0 .6-.4 1-1 1A17 17 0 0 1 3 4c0-.6.4-1 1-1h3.5c.6 0 1 .4 1 1 0 1.3.2 2.5.6 3.6.1.3 0 .7-.2 1z"/></svg>
        <span>+34 611.205.938</span>
      </div>
      <div class="contact__line">
        <svg class="contact__icon" viewBox="0 0 24 24" aria-hidden="true"><rect x="2" y="5" width="20" height="14" rx="1.5" fill="#8dc63f"/><path d="M3 6l9 7 9-7" fill="none" stroke="#fff" stroke-width="1.8"/></svg>
        <span>tommaso.ferlini@brivomatex.example</span>
      </div>
      <div class="contact__line">
        <svg class="contact__icon" viewBox="0 0 24 24" aria-hidden="true"><circle cx="12" cy="12" r="10" fill="#8dc63f"/><path d="M2 12h20M12 2c3 3 3 17 0 20M12 2c-3 3-3 17 0 20" fill="none" stroke="#fff" stroke-width="1.5"/></svg>
        <span>www.brivomatex.example</span>
      </div>
    </div>
  </section>
</main>
</body>
</html>
```